Glass window Vinyl

We are in need of window vinyls for the building shown in the photos. The current vinyls will come down, and we will install the new signage created by this process. We need to advertise:

"Hartwell's Landing Pop Up Market"

Then, below that, it should say for rental inquiries call : 717.555.0193 with our logo which is attached along with our colors and brand guidelines. You may add more color to the Hartwells landing pop up market signage if appropriate. It should be large enough to be easily read from the road by those passing by.

```html
<!DOCTYPE html>
<html lang="en">
<head>
<meta charset="utf-8">
<title>Hartwell's Landing Pop Up Market – Window Vinyl</title>
<link rel="stylesheet" href="https://fonts.googleapis.com/css2?family=Bebas+Neue&display=swap">
<style>
  :root {
    --tan: #9c8560;
    --teal: #0e4250;
    --white: #fcfcfc;
    --band: #ffffff;
  }
  html, body {
    margin: 0;
    padding: 0;
    width: 1200px;
    height: 1200px;
    overflow: hidden;
    background: var(--band);
  }
  .sign {
    display: block;
    width: 1200px;
    height: 1200px;
  }
  .sign text {
    font-family: "Bebas Neue", "Oswald", sans-serif;
  }
  .brand-name { fill: var(--white); letter-spacing: 10px; }
  .brand-sub { fill: var(--white); letter-spacing: 8px; }
  .headline { fill: var(--white); }
  .inquiry { fill: var(--teal); }
  .phone { fill: var(--teal); }
</style>
</head>
<body>
<svg class="sign" viewBox="0 0 1200 1200" xmlns="http://www.w3.org/2000/svg">
  <defs>
    <linearGradient id="split" gradientUnits="userSpaceOnUse" x1="596" y1="486" x2="676" y2="570">
      <stop offset="0" stop-color="var(--tan)" style="stop-color: var(--tan)"/>
      <stop offset="1" stop-color="var(--teal)" style="stop-color: var(--teal)"/>
    </linearGradient>
  </defs>

  <!-- Upper panel -->
  <rect class="panel" x="0" y="0" width="1200" height="1009" fill="url(#split)"/>

  <!-- Brand -->
  <g class="brand">
    <rect class="brand-mark" x="588" y="40" width="24" height="24" fill="var(--white)" style="fill: var(--white)"/>
    <text class="brand-name" x="600" y="137" font-size="44" text-anchor="middle">BRIARWOOD ROW</text>
    <text class="brand-sub" x="600" y="180" font-size="15" text-anchor="middle">PROPERTIES</text>
  </g>

  <!-- Headline -->
  <g class="headline">
    <text x="81" y="425" font-size="282" textLength="1042" lengthAdjust="spacingAndGlyphs">HARTWELL'S</text>
    <text x="81" y="623" font-size="227" textLength="1042" lengthAdjust="spacingAndGlyphs">LANDING POP UP</text>
    <text x="81" y="958" font-size="424" textLength="1038" lengthAdjust="spacingAndGlyphs">MARKET</text>
  </g>

  <!-- Contact band -->
  <rect class="contact-band" x="0" y="1009" width="1200" height="187" fill="var(--band)" style="fill: var(--band)"/>
  <text class="inquiry" x="60" y="1123" font-size="56" textLength="446" lengthAdjust="spacingAndGlyphs">FOR RENTAL INQUIRIES CALL</text>
  <text class="phone" x="551" y="1153" font-size="138" textLength="592" lengthAdjust="spacingAndGlyphs">717.555.0193</text>

  <!-- Base rule -->
  <rect class="base-rule" x="0" y="1196" width="1200" height="4" fill="var(--teal)" style="fill: var(--teal)"/>
</svg>
</body>
</html>
```